Vacation giveaway landing page design

We are giving away a holiday/vacation to Rome and we need a landing page designed that will entice people to enter their email address for a chance to win!

Full brief, examples and everything else can be found in this document: https://files.brintowle.net/papers/p/4-wxkoppTR7mnbQ2vyLazcR5xsjfPe3lhmwcKt27r/view?mode=linked

1 page

```html
<!DOCTYPE html>
<html lang="en">
<head>
<meta charset="utf-8">
<title>Wanderhaus – Win a holiday to Rome</title>
<link rel="stylesheet" href="https://fonts.googleapis.com/css2?family=Anton&family=Abril+Fatface&family=Rubik:wght@400;500;700&display=swap">
<style>
  :root{
    --page-bg:#22223a;
    --white:#ffffff;
    --ink:#2a2a36;
    --form-body:#ccf6fb;
    --yellow:#ffe600;
    --green:#12c94f;
    --red:#f0143c;
  }
  *{box-sizing:border-box;margin:0;padding:0}
  html,body{width:1200px;height:1200px;overflow:hidden;background:var(--page-bg)}
  body{position:relative;font-family:"Rubik",sans-serif;color:var(--white)}

  .hero{position:absolute;left:0;top:0;width:1200px;height:750px;overflow:hidden}
  .hero-photo{position:absolute;inset:0;
    background:
      linear-gradient(180deg,rgba(0,0,0,0) 55%,rgba(20,28,30,.55) 100%),
      linear-gradient(90deg,#c7cfd6 0%,#b9b8bf 30%,#8e969c 52%,#4f6a76 66%,#3e5866 82%,#34505e 100%);}

  .brand{position:absolute;left:0;width:1200px;top:46px;display:flex;justify-content:center;align-items:center;gap:8px}
  .brand-mark{width:22px;height:22px;border:2px solid var(--white);border-radius:50%}
  .brand-name{font-family:"Rubik",sans-serif;font-weight:700;font-size:17px;letter-spacing:1px;text-transform:uppercase}

  .offer{position:absolute;left:142px;top:130px;font-family:"Anton",sans-serif;font-weight:400;font-size:55px;line-height:1;letter-spacing:-1px;white-space:nowrap}
  .destination{position:absolute;left:138px;top:170px;font-family:"Abril Fatface",serif;font-weight:400;font-size:124px;line-height:1;letter-spacing:-2px}
  .destination .dot{color:var(--yellow)}

  .signup-card{position:absolute;left:142px;top:303px;width:455px;height:256px;background:var(--form-body);border-radius:2px;overflow:hidden}
  .signup-head{height:63px;background:var(--white);display:flex;align-items:center;justify-content:space-between;padding:0 21px}
  .signup-title{color:var(--ink);font-weight:500;font-size:18.5px}
  .signup-body{padding:27px 21px 0}
  .field-label{color:var(--ink);font-size:13px;font-weight:400}
  .field-label b{font-weight:500}
  .fields{display:flex;gap:11px;margin-top:12px}
  .field{flex:1;height:33px;background:var(--white);border-radius:2px;display:flex;align-items:center;padding:0 11px;color:var(--ink);font-size:13px}
  .signup-btn{position:absolute;right:22px;top:191px;width:155px;height:43px;background:var(--yellow);border-radius:2px;display:flex;align-items:center;justify-content:center;gap:14px;color:var(--ink);font-weight:700;font-size:20px}

  .share{position:absolute;left:142px;top:606px;display:flex;align-items:center;gap:12px;font-size:13px;font-weight:500}
  .share-link{display:flex;align-items:center;gap:4px;font-size:11px;font-weight:500}
  .share-link::before{content:"";width:7px;height:7px;border-radius:50%;background:var(--white)}

  .prize{position:absolute;right:142px;top:356px;text-align:right}
  .prize-badge{display:inline-block;background:var(--green);color:var(--white);font-weight:700;font-size:11.5px;padding:7px 15px;border-radius:1px}
  .prize-title{font-family:"Abril Fatface",serif;font-weight:400;font-size:62px;line-height:61px;margin-top:8px;letter-spacing:-1px}
  .prize-sub{font-family:"Anton",sans-serif;color:var(--yellow);font-size:14px;letter-spacing:7.5px;margin-top:14px;margin-right:-7px}

  .perks{position:absolute;left:0;top:750px;width:1200px;height:450px;background:var(--page-bg)}
  .perks-title{position:absolute;left:0;width:1200px;top:48px;text-align:center;font-family:"Anton",sans-serif;font-weight:400;font-size:48px;letter-spacing:-1px;color:var(--red)}
  .perk-icons{position:absolute;top:130px;left:0;width:1200px;display:flex;justify-content:space-around;padding:0 110px}
  .perk-icons svg{width:52px;height:52px}
</style>
</head>
<body>
  <section class="hero">
    <div class="hero-photo" role="img" aria-label="Photo of Rome at dusk: rooftops and trees on the left, a carved marble monument with statues on the right"></div>

    <header class="brand">
      <span class="brand-mark"></span>
      <span class="brand-name">Wanderhaus</span>
    </header>

    <h2 class="offer">4 NIGHTS, 2 PEOPLE</h2>
    <h1 class="destination">Rome<span class="dot">.</span></h1>

    <form class="signup-card">
      <div class="signup-head">
        <span class="signup-title">Please fill in your details below</span>
        <svg width="22" height="22" viewBox="0 0 22 22" fill="none" stroke="#2a2a36" stroke-width="1.3"><path d="M3 19l1.2-4.5L15.5 3.2l3.3 3.3L7.5 17.8z"/><path d="M13.5 5.2l3.3 3.3"/><path d="M4.2 14.5l3.3 3.3"/></svg>
      </div>
      <div class="signup-body">
        <p class="field-label"><b>Name</b> and <b>Email address</b></p>
        <div class="fields">
          <span class="field">Full name</span>
          <span class="field">yourname@inbox.test</span>
        </div>
      </div>
      <div class="signup-btn">Signup
        <svg width="20" height="18" viewBox="0 0 20 18" fill="none" stroke="#12c94f" stroke-width="3" stroke-linecap="round" stroke-linejoin="round"><path d="M2 9h15M10 2l7 7-7 7"/></svg>
      </div>
    </form>

    <div class="share">
      <span>Share this deal</span>
      <span class="share-link">Koda</span>
      <span class="share-link">Velo</span>
      <span class="share-link">Lumo</span>
      <span class="share-link">Brisk</span>
      <span class="share-link">Reelo</span>
    </div>

    <div class="prize">
      <span class="prize-badge">Worth of $130,-</span>
      <p class="prize-title">join and<br>win a holiday</p>
      <p class="prize-sub">WEEKLY NEW VACATION PRIZES</p>
    </div>
  </section>

  <section class="perks">
    <h2 class="perks-title">JOIN &amp; GET</h2>
    <div class="perk-icons">
      <svg viewBox="0 0 52 52" fill="none" stroke="#f0143c" stroke-width="2.5"><rect x="4" y="12" width="44" height="28" rx="2"/><path d="M30 12v28"/><path d="M35 20h8M35 26h8M35 32h8"/><path d="M10 30l12-10M14 20l4 4"/></svg>
      <svg viewBox="0 0 52 52" fill="none" stroke="#f0143c" stroke-width="2.5"><rect x="10" y="14" width="32" height="32"/><path d="M4 46h44"/><rect x="20" y="6" width="12" height="8"/><path d="M16 22h4M24 22h4M32 22h4M16 30h4M24 30h4M32 30h4M22 46v-8h8v8"/></svg>
      <svg viewBox="0 0 52 52" fill="none" stroke="#f0143c" stroke-width="2.5"><rect x="8" y="10" width="36" height="32"/><path d="M8 38l12-12 8 8 6-6 10 10"/><circle cx="32" cy="19" r="3"/></svg>
      <svg viewBox="0 0 52 52" fill="none" stroke="#f0143c" stroke-width="2.5"><circle cx="26" cy="22" r="15"/><circle cx="26" cy="22" r="10"/><path d="M24 19l3-2v10M18 35l-4 12 6-3 4 5 2-10M34 35l4 12-6-3-4 5-2-10"/></svg>
    </div>
  </section>
</body>
</html>
```